Business Cards for new orthopaedic surgery practice

My husband and I are starting our own orthopaedic surgery practice. We are looking for a business card that is uniform, but one will have my name/title and the other will have his. You can just create one design with my name on it for now. But when I choose your design as the winning design I will ask that you add another copy with his name/title.

We are looking for classy, simple, elite all in one. We like dark blues/a little gold/yellow. Something that goes with our logo. We want our logo incorporated. Here is all the info you need:
Business name: RV Spine & Vitality Center
Location: 38915 North Bramble Ave
Palm Crest, FL 33990
Phone: 954-218-4630
Fax: 954-571-2846
Email: info@myrvspine.example

Names: Lucinda Ferrow, M.D.
Board Certified Hand and Upper Extremity Surgeon

Emeka Dlunga, M.D.
Board Certified Hip & Knee Replacement/General Orthopaedic Surgeon

Can decide what you want to put on the back. Maybe a slogan:
Grounded in Trust. Built for You

I am just going to upload our logo. The only thing is if we select you as the winning design, the location, and phone numbers may change. We will need your help to update that once fully solidified.

Industry/Entity Type

Medical

Contact Information for Business Card

Colors
0054AA
0677BA
7BADD7
CADEEF
E8F1F8
0094D4
00A9DD
6FCCEA
C7EBF8
E9F6FB

Requirements
Must have
• class, appeal,
Should not have
• We want to air on the side of masculine if we are looking at masculine vs. feminine feel. But we still want it classy, sophisticated, and something we will love

```html
<!DOCTYPE html>
<html lang="en">
<head>
<meta charset="utf-8">
<title>RV Spine &amp; Vitality Center — Business Card</title>
<link rel="stylesheet" href="https://fonts.googleapis.com/css2?family=Alegreya+Sans:wght@400;500&family=Source+Sans+3:wght@400&display=swap">
<style>
  :root {
    --page-bg: #e4e5e7;
    --card-navy: #223a63;
    --accent-teal: #2fb4c9;
    --text-white: #f4f6f9;
    --rule-gold: #b8964c;
  }
  * { margin: 0; padding: 0; box-sizing: border-box; }
  html, body { width: 1017px; height: 1200px; overflow: hidden; }
  body {
    position: relative;
    background: var(--page-bg);
    font-family: "Alegreya Sans", "Source Sans 3", sans-serif;
    color: var(--text-white);
  }
  .card {
    position: absolute;
    left: 99px;
    width: 817px;
    background: var(--card-navy);
  }
  .card--front { top: 76px; height: 497px; }
  .card--back { top: 624px; height: 501px; }

  .brand {
    position: absolute;
    left: 0; right: 0;
    display: flex;
    align-items: center;
    justify-content: center;
    gap: 16px;
    font-family: "Alegreya Sans", sans-serif;
    font-weight: 500;
    font-size: 32px;
    letter-spacing: 0.5px;
    transform: translateY(-50%);
  }
  .brand__dot { width: 26px; height: 26px; border-radius: 50%; }
  .card--front .brand { top: 273px; color: var(--accent-teal); }
  .card--front .brand__dot { background: var(--accent-teal); }
  .card--back .brand { top: 145px; color: var(--text-white); }
  .card--back .brand__dot { background: var(--text-white); }

  .slogan {
    position: absolute;
    top: 419px; left: 0; right: 0;
    transform: translateY(-50%);
    text-align: center;
    font-size: 27px;
  }
  .doctor-name {
    position: absolute;
    top: 263px; left: 0; right: 0;
    transform: translateY(-50%);
    text-align: center;
    font-size: 30px;
    font-weight: 400;
  }
  .doctor-title {
    position: absolute;
    top: 298px; left: 0; right: 0;
    transform: translateY(-50%);
    text-align: center;
    font-size: 21px;
  }
  .gold-rule {
    position: absolute;
    top: 376px; left: 73px; right: 78px;
    height: 3px;
    background: var(--rule-gold);
  }
  .contact, .address {
    position: absolute;
    font-family: "Source Sans 3", sans-serif;
    font-size: 21px;
    line-height: 26px;
  }
  .contact { top: 388px; left: 73px; list-style: none; }
  .address { top: 402px; right: 78px; text-align: right; font-size: 22px; line-height: 29px; font-style: normal; }
  .contact__label { display: inline-block; width: 26px; }
</style>
</head>
<body>
  <section class="card card--front">
    <div class="brand"><span class="brand__dot"></span><span class="brand__name">RV Spine &amp; Vitality Center</span></div>
    <p class="slogan">Grounded in Trust. Built for You</p>
  </section>

  <section class="card card--back">
    <div class="brand"><span class="brand__dot"></span><span class="brand__name">RV Spine &amp; Vitality Center</span></div>
    <h1 class="doctor-name">Lucinda Ferrow, M.D.</h1>
    <p class="doctor-title">Board Certified Hand and Upper Extremity Surgeon</p>
    <div class="gold-rule"></div>
    <ul class="contact">
      <li><span class="contact__label">P:</span>954-218-4630</li>
      <li><span class="contact__label">F:</span>954-571-2846</li>
      <li><span class="contact__label">E:</span>info@myrvspine.example</li>
    </ul>
    <address class="address">
      38915 North Bramble Ave<br>
      Palm Crest, FL 33990
    </address>
  </section>
</body>
</html>
```